label design for soy candle

I am a start up making soy candles and other products involving scents.
On the label should be in writing : the scent, Handgemacht in der Schweiz, Sojakerze, my logo with the name Thorvel Candles on it. I will upload the currant label of my candles, but I want something more fashioned. The color of the label should be black with the scent written in gold, and the rest in white. Or maybe suggest something different, I am open to new designs. I am also open to change the logo, except the flower has to stay.
Sizes : square 60x60mm / round 50mm / rectangle 70x20mm ( for different jars )

```html
<!DOCTYPE html>
<html lang="de">
<head>
<meta charset="utf-8">
<title>Thorvel Candles – Sojakerze Etikett</title>
<link rel="stylesheet" href="https://fonts.googleapis.com/css2?family=Poiret+One&family=Mr+Dafoe&family=Poppins:wght@200;300&display=swap">
<style>
  :root {
    --page: #ffffff;
    --label-black: #0f0f0f;
    --rim-gold: #d6b03a;
    --scent-gold: #d9b53c;
    --cream: #f3e4b4;
  }
  html, body {
    margin: 0;
    width: 1200px;
    height: 1200px;
    overflow: hidden;
    background: var(--page);
  }
  .label {
    position: relative;
    width: 1200px;
    height: 1200px;
  }
  .label__disc {
    position: absolute;
    inset: 0;
  }
  .brand {
    position: absolute;
    left: 0;
    right: 0;
    text-align: center;
  }
  .brand__dot {
    position: absolute;
    top: 178px;
    left: 582px;
    width: 36px;
    height: 36px;
    border-radius: 50%;
    background: var(--cream);
  }
  .brand__rule {
    position: absolute;
    top: 278px;
    left: 294px;
    width: 592px;
    height: 4px;
    background: var(--cream);
  }
  .brand__name {
    top: 296px;
    margin: 0;
    font-family: "Poiret One", sans-serif;
    font-weight: 400;
    font-size: 132px;
    line-height: 1.1;
    color: var(--cream);
    letter-spacing: 2px;
  }
  .scent {
    position: absolute;
    top: 470px;
    left: 0;
    right: 0;
    margin: 0;
    text-align: center;
    font-family: "Mr Dafoe", cursive;
    font-weight: 400;
    font-size: 300px;
    line-height: 1;
    color: var(--scent-gold);
  }
  .product-type {
    position: absolute;
    top: 866px;
    left: 0;
    right: 0;
    margin: 0;
    text-align: center;
    font-family: "Poppins", sans-serif;
    font-weight: 300;
    font-size: 44px;
    letter-spacing: 11px;
    color: var(--cream);
  }
  .origin {
    position: absolute;
    top: 932px;
    left: 0;
    right: 0;
    margin: 0;
    text-align: center;
    font-family: "Poppins", sans-serif;
    font-weight: 200;
    font-size: 48px;
    color: var(--cream);
  }
</style>
</head>
<body>
  <main class="label">
    <svg class="label__disc" width="1200" height="1200" viewBox="0 0 1200 1200" aria-hidden="true">
      <circle cx="600" cy="600" r="591" fill="var(--label-black)" stroke="var(--rim-gold)" stroke-width="10"/>
    </svg>

    <div class="brand__dot" aria-hidden="true"></div>
    <div class="brand__rule" aria-hidden="true"></div>
    <h1 class="brand brand__name">Thorvel Candles</h1>

    <p class="scent">Scent</p>

    <p class="product-type">SOJAKERZE</p>
    <p class="origin">Handgemacht in der Schweiz</p>
  </main>
</body>
</html>
```